Wordpress Design For Financial Investment Company

//** NEW WIREFRAME ADDED TO HELP WITH LAYOUT ISSUES. PLEASE REFER TO WIREFRAME IN ATTACHED FILES. NO DESIGN WILL BE CONSIDERED IF IT DOES NOT FOLLOW THE WIREFRAME. **//
//** PLEASE READ THE ENTIRE BRIEF INCLUDING ALL UPDATES TO THE BRIEF. THE CLIENT IS VERY SPECIFIC ABOUT WHAT THEY WANT AND I'VE COVERED SEVERAL THINGS IN THE UPDATES. THERE IS ALSO A VIDEO UPDATE THAT HAS SOME VALUABLE INFORMATION IN IT FOR THIS CONTEST. **//
The client is an investment advisor who needs a new website designed. The current site is http://www.velmorfield.net.
The client wants the site to be green to match the attached logo.
The home page should have relevant images in the rotator. No people hugging! This is a financial investment site, not a family counseling site.
Also, the client wants 4 buttons on the home page to highlight the 4 main areas they focus on:
Investment Advice and Education
General Financial Planning
Retirement Planning
401K Planning
The top right area of the site needs to have their phone number, a call to action, and 2 buttons.
Their phone number is 303-418-7639
The call to action should say something like "Call for a free consultation!"
The buttons need to say:
Login To Your Bluvexa Account
Login To Your Quillbrook Account
The final design should communicate professionalism, financial safety and growth.
Main navigation should be:
Home
About Us
Associates
Services
Contact
Mission Statement (Could also be "Our Mission")
This is a site that the client likes: http://www.pwkinvestmentconsulting.com/
Updates
The designs should not have:
Newsletter content. A newsletter sign up is fine
Learning Center
Calculators
Stock prices/tickers
The design should have a contact form on the page.
I have talked to my client and have some updates. I did a video update because I thought it would be easier to show what I'm trying to get across.
Reason: I am going to be extending the contest a few more days. I'm still not getting quite what I want and very few people are even trying to follow the creative brief and the updates to it.
PLEASE read the entire brief and the updates. There is also a video I made that explains everything. I've also attached a wireframe.
Thanks!
Target Market(s)
People looking for a high-end financial investment company.
Industry/Entity Type
Investment
Requirements
Must have
- !!FOLLOW THE WIREFRAME FOR LAYOUT!!
!!THEIR LOGO!!
4 buttons to highlight their main practice areas
Phone number in the top right
"Free Consultation" call to action
2 Login buttons in the top right
A contact form on the page.
Should not have
- The designs should not have:
Learning Center
Calculators
Stock prices/tickers

```html
<!DOCTYPE html>
<html lang="en">
<head>
<meta charset="utf-8">
<title>Velmorfield Financial</title>
<link href="https://fonts.googleapis.com/css2?family=Oswald:wght@400&family=Source+Sans+3:wght@400;600&display=swap" rel="stylesheet">
<style>
:root{
  --green:#8fbc14;
  --green-dark:#6f9a0a;
  --green-light:#a8d22a;
  --ink:#1e1e1e;
  --muted:#666;
  --nav:#141414;
  --line:#9a9a9a;
  --field:#fff;
  --field-border:#ccc;
}
*{margin:0;padding:0;box-sizing:border-box}
html,body{width:1182px;height:1200px;overflow:hidden}
body{position:relative;background:#fff;font-family:"Source Sans 3",Arial,sans-serif;color:var(--ink)}
.abs{position:absolute}
.header-bg{left:0;top:0;width:1182px;height:132px;background:linear-gradient(#fff,#ececec)}
.brand{left:157px;top:40px;display:flex;align-items:center;gap:10px}
.brand-dot{width:48px;height:48px;border-radius:50%;background:var(--green)}
.brand-name{font-size:24px;font-weight:600;color:var(--green-dark)}
.login{top:11px;width:164px;height:49px;background:linear-gradient(var(--green-light),var(--green-dark));border-radius:3px;color:#fff;font-family:"Oswald",sans-serif;font-size:16px;line-height:18px;padding:7px 11px;text-transform:uppercase;box-shadow:0 1px 3px rgba(0,0,0,.3)}
.callbox{left:678px;top:79px;width:345px;height:35px;background:linear-gradient(#fff,#eee);border:1px solid #ddd;border-radius:3px;box-shadow:0 2px 3px rgba(0,0,0,.2);display:flex;align-items:center;padding-left:12px;gap:8px;font-size:15px;color:#222}
.callbox .phone{font-size:20px;color:var(--green-dark);margin-left:4px}
.nav-bar{left:0;top:132px;width:1182px;height:27px;background:linear-gradient(#3a3a3a,var(--nav))}
.nav-menu{left:160px;top:132px;width:650px;height:27px;display:flex;list-style:none}
.nav-menu li{flex:1;color:#fff;font-size:12px;text-transform:uppercase;text-align:center;line-height:27px;border-right:1px solid #555;white-space:nowrap}
.nav-menu li:last-child{border-right:none}
.search{left:817px;top:132px;width:206px;height:27px;background:#fff;border-radius:3px 0 0 3px}
.search-btn{left:965px;top:132px;width:58px;height:27px;background:var(--green);color:#222;font-size:12px;text-align:center;line-height:27px}
.hero-band{left:0;top:159px;width:1182px;height:321px;background:linear-gradient(#e6e6e6,#f6f6f6)}
.hero-frame{left:162px;top:172px;width:862px;height:342px;background:#fff;box-shadow:0 6px 14px rgba(0,0,0,.25)}
.hero-photo{left:166px;top:176px;width:853px;height:333px;background:linear-gradient(120deg,#b9bf9a,#d8d3c2 45%,#a89c7e 75%,#5a5040)}
.hero-caption{left:172px;top:465px;width:843px;height:41px;background:rgba(60,60,60,.6);color:#fff;font-size:27px;text-align:center;line-height:41px;text-transform:uppercase;white-space:nowrap}
.arrow{top:324px}
.section-title{left:165px;top:535px;font-size:20px;font-weight:400}
.dash{height:0;border-top:1px dashed var(--line)}
.intro-photo{left:167px;top:588px;width:168px;height:112px;background:linear-gradient(90deg,#8a8a8a,#dcdcdc 45%,#b7c7d8)}
.intro-text{left:351px;top:581px;width:423px;font-size:12.5px;line-height:20px;text-align:justify}
.panel{top:796px;left:168px;width:607px;height:251px;background:#f1f1f1;border:1px solid #ddd;border-radius:3px;overflow:hidden}
.panel-head{height:30px;background:linear-gradient(#6a6a6a,#3c3c3c);color:#fff;font-size:17px;line-height:30px;padding-left:10px}
.contact-form{display:grid;grid-template-columns:1fr 1fr;gap:10px 14px;padding:14px 14px}
.contact-form label{display:block;font-size:12px;color:var(--muted);margin-bottom:3px}
.field{height:26px;background:var(--field);border:1px solid var(--field-border);border-radius:3px}
.field.message{height:74px}
.form-wide{grid-column:1 / 3;display:grid;grid-template-columns:1fr 110px;gap:14px;align-items:end}
.send-btn{height:28px;background:linear-gradient(var(--green-light),var(--green-dark));color:#fff;font-size:13px;text-align:center;line-height:28px;border-radius:2px}
.focus{left:814px;width:209px;background:linear-gradient(var(--green-light),var(--green));color:#fff;font-size:21px;line-height:25px;padding:8px 18px;border-radius:2px;box-shadow:0 2px 3px rgba(0,0,0,.25)}
.focus svg{position:absolute;right:12px;bottom:10px}
.signup-title{left:816px;top:894px;font-size:21px;font-weight:400}
.signup-text{left:817px;top:926px;width:205px;font-size:12px;line-height:17px;color:#333}
.signup-input{left:818px;top:983px;width:200px;height:24px;background:linear-gradient(#fff,#ececec);border:1px solid var(--field-border);border-radius:3px;box-shadow:0 1px 2px rgba(0,0,0,.2)}
.signup-btn{left:934px;top:1020px;width:84px;height:26px;background:linear-gradient(var(--green-light),var(--green-dark));color:#fff;font-size:12px;text-align:center;line-height:26px;border-radius:2px}
.footer{left:0;top:1064px;width:1182px;height:136px;background:linear-gradient(#3a3a3a,#1e1e1e)}
.foot-title{top:1082px;color:#fff;font-size:12px;font-weight:600}
.foot-text{left:170px;top:1106px;color:#bbb;font-size:11.5px;line-height:18px}
.foot-rule{left:168px;top:1157px;width:852px;height:1px;background:#444}
.foot-links{left:170px;top:1171px;color:#bbb;font-size:10.5px}
.foot-copy{right:162px;top:1171px;color:#bbb;font-size:10.5px}
.social{top:1110px;width:22px;height:22px;border-radius:3px;background:#8a8a8a}
</style>
</head>
<body>
<header>
<div class="abs header-bg"></div>
<div class="abs brand"><span class="brand-dot"></span><span class="brand-name">Velmorfield Financial</span></div>
<div class="abs login" style="left:688px">Login to your<br>Bluvexa account</div>
<div class="abs login" style="left:859px">Login to your<br>Quillbrook account</div>
<div class="abs callbox">
  <svg width="20" height="20" viewBox="0 0 20 20"><rect x="1" y="3" width="5" height="15" rx="1" fill="#333"/><rect x="7" y="6" width="12" height="12" rx="1" fill="#555"/><rect x="9" y="8" width="8" height="3" fill="#ddd"/><g fill="#ddd"><rect x="9" y="13" width="2" height="2"/><rect x="12" y="13" width="2" height="2"/><rect x="15" y="13" width="2" height="2"/></g></svg>
  <span>Call for a free consultation!</span><span class="phone">303-418-7639</span>
</div>
</header>

<nav>
<div class="abs nav-bar"></div>
<ul class="abs nav-menu">
  <li>Home</li><li>About Us</li><li>Associates</li><li>Services</li><li>Contact</li><li>Our Mission</li>
</ul>
<div class="abs search"><svg style="position:absolute;left:8px;top:6px" width="15" height="15" viewBox="0 0 15 15"><circle cx="6" cy="6" r="4" fill="none" stroke="#888" stroke-width="1.6"/><line x1="9" y1="9" x2="14" y2="14" stroke="#666" stroke-width="2"/></svg></div>
<div class="abs search-btn">SEARCH</div>
</nav>

<div class="abs hero-band"></div>
<div class="abs hero-frame"></div>
<div class="abs hero-photo" role="img" aria-label="Photo of a retired couple on a sofa meeting with a financial advisor"></div>
<svg class="abs arrow" style="left:189px" width="54" height="54" viewBox="0 0 54 54"><circle cx="27" cy="27" r="27" fill="rgba(30,30,30,.75)"/><path d="M31 16 L20 27 L31 38" fill="none" stroke="#fff" stroke-width="4"/></svg>
<svg class="abs arrow" style="left:947px" width="54" height="54" viewBox="0 0 54 54"><circle cx="27" cy="27" r="27" fill="rgba(30,30,30,.75)"/><path d="M23 16 L34 27 L23 38" fill="none" stroke="#fff" stroke-width="4"/></svg>
<div class="abs hero-caption">50% of retirees left the workforce earilet than planned.</div>

<h2 class="abs section-title">Welcome to Our Site</h2>
<div class="abs dash" style="left:168px;top:567px;width:603px"></div>
<div class="abs intro-photo" role="img" aria-label="Photo of an advisor meeting a couple at their home"></div>
<p class="abs intro-text">Velmorfield Financial is a Registered Investment Advisor whose principle is a Certified Financial Planner with over 26 years of experience. We are fee based Advisors and we work to create investment programs that are suitable to you. We provide superior investment management and financial planning services for all of our clients. We provide our clients with a fiduciary level of service and we have an obligation to act in an investors best interest in all aspects of the financial relationship. We provide individualized services where we educate our clients and assist in implementation of actions which enhance our clients emotional and financial well being.</p>
<div class="abs dash" style="left:168px;top:776px;width:603px"></div>

<section class="abs panel">
  <div class="panel-head">Contact Us</div>
  <div class="contact-form">
    <div><label>Name</label><div class="field"></div></div>
    <div><label>Email</label><div class="field"></div></div>
    <div class="form-wide">
      <div><label>Message</label><div class="field message"></div></div>
      <div class="send-btn">SEND</div>
    </div>
  </div>
</section>

<div class="abs focus" style="top:545px;height:90px">Investment Advice and Education<svg width="22" height="22" viewBox="0 0 22 22"><circle cx="11" cy="11" r="10" fill="#eee" stroke="#fff" stroke-width="1.5"/><path d="M7 7 L11 11 L7 15z M11 7 L15 11 L11 15z" fill="#555"/></svg></div>
<div class="abs focus" style="top:647px;height:68px">General Financial Planning<svg width="22" height="22" viewBox="0 0 22 22"><circle cx="11" cy="11" r="10" fill="#eee" stroke="#fff" stroke-width="1.5"/><path d="M7 7 L11 11 L7 15z M11 7 L15 11 L11 15z" fill="#555"/></svg></div>
<div class="abs focus" style="top:727px;height:68px">Retirement<br>Planning<svg width="22" height="22" viewBox="0 0 22 22"><circle cx="11" cy="11" r="10" fill="#eee" stroke="#fff" stroke-width="1.5"/><path d="M7 7 L11 11 L7 15z M11 7 L15 11 L11 15z" fill="#555"/></svg></div>
<div class="abs focus" style="top:807px;height:68px">401K<br>Planning<svg width="22" height="22" viewBox="0 0 22 22"><circle cx="11" cy="11" r="10" fill="#eee" stroke="#fff" stroke-width="1.5"/><path d="M7 7 L11 11 L7 15z M11 7 L15 11 L11 15z" fill="#555"/></svg></div>

<h2 class="abs signup-title">Newsletter Sign Up</h2>
<p class="abs signup-text">Enter your email to receive our updates and planning tips.</p>
<div class="abs signup-input"></div>
<div class="abs signup-btn">SUBSCRIBE</div>

<footer>
<div class="abs footer"></div>
<div class="abs foot-title" style="left:169px">Contact Us</div>
<div class="abs foot-text">2240 Aldren Parkway #210, Marlow Village, CO 80190<br>Phone: 303-418-7639 800-555-0192, Fax: 303-555-0147</div>
<div class="abs foot-title" style="left:954px">Follow Us On</div>
<span class="abs social" style="left:912px"></span>
<span class="abs social" style="left:942px"></span>
<span class="abs social" style="left:971px"></span>
<span class="abs social" style="left:998px"></span>
<div class="abs foot-rule"></div>
<div class="abs foot-links">Home &nbsp;\ &nbsp;About Us &nbsp;\ &nbsp;Associates &nbsp;\ &nbsp;Services &nbsp;\ &nbsp;Contact &nbsp;\ &nbsp;Our Mission</div>
<div class="abs foot-copy">Copyrights @ 2013 All Rights Reserved</div>
</footer>
</body>
</html>
```